Morquel Business Card (intended for Business Card sized magnet)

Hi guys,

I would like to get a design for my business card for the restaurant. The design must be single sided as I intend to produce business card sized magnets.

The File attached must me on and I'm open for new ides

Can you please ensure that the design meets Prindlecraft's magnetic business card size specifications:

http://www.prindlecraft.example/custom-magnets.aspx?txi=15695&xnid=TopNav_Magnetic+Business+Cards+(linked+item)_Magnets_Marketing+Products&xnav=TopNav

Full Bleed Size (starting document size):
90 x 52 mm
1062 x 615 pixels
* Finished artwork should use the full bleed dimensions for best results.

Document Trim Size (final size after being cut):
87 x 49 mm
1028 x 579 pixels
* Please be sure to keep all text within the safe margin.

Resolution:
300 DPI

The winning design/source files need to meet these specifications.

Thanks
Updates

Hi guys, can I see more options please Thanks

Industry/Entity Type

Business

```html
<!DOCTYPE html>
<html lang="en">
<head>
<meta charset="utf-8">
<title>Morquel Business Cards</title>
<link href="https://fonts.googleapis.com/css2?family=PT+Serif:ital@0;1&family=Open+Sans:wght@400&display=swap" rel="stylesheet">
<style>
  :root {
    --page: #e4e4e2;
    --ink: #111111;
    --black-panel: #0c0c0c;
    --dark-band: #1d1d1d;
    --stone: #d6d6d4;
    --stone-band: #b9b9b7;
    --ornament-band: #a9a9a7;
    --paper: #f4f4f2;
    --paper-band: #cacac8;
    --light-text: #d8d8d8;
    --rule: #111111;
  }
  * { box-sizing: border-box; margin: 0; padding: 0; }
  html, body { width: 1200px; height: 1000px; overflow: hidden; }
  body { background: var(--page); position: relative; font-family: "Open Sans", sans-serif; }

  .card {
    position: absolute; left: 250px; width: 700px; height: 394px;
    overflow: hidden; box-shadow: 0 6px 18px rgba(0,0,0,0.18);
  }
  .card--dark { top: 70px; background: var(--stone); }
  .card--light { top: 536px; background: var(--paper); }

  .logo { font-family: "PT Serif", serif; font-weight: 400; color: var(--ink); line-height: 1; }

  .person-name { font-family: "PT Serif", serif; font-size: 24px; line-height: 1.1; }
  .person-title { font-family: "PT Serif", serif; font-style: italic; font-size: 15px; }

  .contact-list { list-style: none; font-size: 13px; line-height: 1; }
  .contact-list li { display: flex; align-items: center; gap: 10px; height: 22px; }
  .contact-list svg { width: 13px; height: 13px; flex: none; }

  /* dark card */
  .dark-panel { position: absolute; left: 0; top: 0; width: 385px; height: 394px; background: var(--black-panel); color: var(--light-text); }
  .dark-panel .identity { position: absolute; right: 34px; top: 40px; text-align: right; }
  .dark-panel .contact-list { position: absolute; left: 32px; top: 150px; color: var(--light-text); }
  .dark-panel .contact-list svg { fill: var(--light-text); stroke: var(--light-text); }
  .dark-ornament { position: absolute; left: 0; top: 292px; width: 385px; height: 82px; background: var(--dark-band); }

  .stone-panel { position: absolute; left: 385px; top: 0; width: 315px; height: 394px; }
  .stone-panel .logo { position: absolute; left: 34px; top: 30px; font-size: 64px; }
  .stone-panel .rule-a { position: absolute; left: 0; right: 0; top: 130px; height: 2px; background: var(--rule); }
  .stone-panel .colour-ornament { position: absolute; left: 0; right: 0; top: 138px; height: 88px; background: var(--ornament-band); }
  .stone-panel .rule-b { position: absolute; left: 0; right: 0; top: 232px; height: 2px; background: var(--rule); }
  .stone-ornament { position: absolute; left: -385px; right: 0; top: 292px; height: 82px; }
  .stone-panel .stone-ornament { left: 0; background: var(--stone-band); }
  .edge-stripe { position: absolute; left: 0; right: 0; bottom: 0; height: 14px; background: var(--black-panel); }

  /* light card */
  .brand-block { position: absolute; left: 0; top: 0; width: 300px; height: 140px; border-right: 2px solid var(--rule); border-bottom: 2px solid var(--rule); }
  .brand-block .logo { position: absolute; left: 28px; top: 14px; font-size: 56px; }
  .brand-block .colour-ornament { position: absolute; left: 0; right: 0; bottom: 8px; height: 50px; background: var(--ornament-band); }
  .card--light .contact-list { position: absolute; left: 30px; top: 156px; color: var(--ink); }
  .card--light .contact-list svg { fill: var(--ink); stroke: var(--ink); }
  .card--light .identity { position: absolute; right: 42px; top: 160px; text-align: right; color: var(--ink); }
  .paper-rule { position: absolute; left: 0; right: 0; top: 262px; height: 2px; background: var(--rule); }
  .paper-ornament { position: absolute; left: 0; right: 0; top: 276px; height: 74px; background: var(--paper-band); }
  .paper-rule--lower { top: 362px; }
</style>
</head>
<body>

  <section class="card card--dark">
    <div class="dark-panel">
      <div class="identity">
        <p class="person-name">K.Suranel</p>
        <p class="person-title">My Title</p>
      </div>
      <ul class="contact-list">
        <li><svg viewBox="0 0 12 12"><path d="M6 0.5a3.8 3.8 0 0 0-3.8 3.8C2.2 7.2 6 11.5 6 11.5s3.8-4.3 3.8-7.2A3.8 3.8 0 0 0 6 0.5zm0 5.3a1.5 1.5 0 1 1 0-3 1.5 1.5 0 0 1 0 3z" stroke="none"/></svg>412, Larkmoor Rd, Ashvale North, 3190</li>
        <li><svg viewBox="0 0 12 12" fill="none"><circle cx="6" cy="6" r="5" fill="none" stroke-width="1.2"/><path d="M1 6h10M6 1c-2.5 3-2.5 7 0 10M6 1c2.5 3 2.5 7 0 10" fill="none" stroke-width="1"/></svg>www.morquel.example</li>
        <li><svg viewBox="0 0 12 12"><rect x="0.5" y="2" width="11" height="8" stroke="none"/><path d="M0.8 2.4 6 6.6l5.2-4.2" fill="none" stroke="#0c0c0c" stroke-width="1"/></svg>hello@morquel.example</li>
        <li><svg viewBox="0 0 12 12"><path d="M2.6 0.8 4.6 3 3.6 4.4c.7 1.6 2.2 3.1 3.9 3.9l1.4-1 2.2 2-.9 1.9C6 11 1 6 .9 1.7z" stroke="none"/></svg>03 9000 4127</li>
      </ul>
      <div class="dark-ornament" role="img" aria-label="Dark geometric star lattice border"></div>
    </div>
    <div class="stone-panel">
      <p class="logo">Morquel</p>
      <div class="rule-a"></div>
      <div class="colour-ornament" role="img" aria-label="Geometric star lattice border with red, teal and yellow accents"></div>
      <div class="rule-b"></div>
      <div class="stone-ornament" role="img" aria-label="Light grey geometric star lattice border"></div>
    </div>
    <div class="edge-stripe"></div>
  </section>

  <section class="card card--light">
    <div class="brand-block">
      <p class="logo">Morquel</p>
      <div class="colour-ornament" role="img" aria-label="Geometric star lattice border with red, teal and yellow accents"></div>
    </div>
    <ul class="contact-list">
      <li><svg viewBox="0 0 12 12"><path d="M6 0.5a3.8 3.8 0 0 0-3.8 3.8C2.2 7.2 6 11.5 6 11.5s3.8-4.3 3.8-7.2A3.8 3.8 0 0 0 6 0.5zm0 5.3a1.5 1.5 0 1 1 0-3 1.5 1.5 0 0 1 0 3z" stroke="none"/></svg>412, Larkmoor Rd, Ashvale North, 3190</li>
      <li><svg viewBox="0 0 12 12"><circle cx="6" cy="6" r="5" fill="none" stroke-width="1.2"/><path d="M1 6h10M6 1c-2.5 3-2.5 7 0 10M6 1c2.5 3 2.5 7 0 10" fill="none" stroke-width="1"/></svg>www.morquel.example</li>
      <li><svg viewBox="0 0 12 12"><rect x="0.5" y="2" width="11" height="8" stroke="none"/><path d="M0.8 2.4 6 6.6l5.2-4.2" fill="none" stroke="#f4f4f2" stroke-width="1"/></svg>hello@morquel.example</li>
      <li><svg viewBox="0 0 12 12"><path d="M2.6 0.8 4.6 3 3.6 4.4c.7 1.6 2.2 3.1 3.9 3.9l1.4-1 2.2 2-.9 1.9C6 11 1 6 .9 1.7z" stroke="none"/></svg>03 9000 4127</li>
    </ul>
    <div class="identity">
      <p class="person-name">K.Suranel</p>
      <p class="person-title">My Title</p>
    </div>
    <div class="paper-rule"></div>
    <div class="paper-ornament" role="img" aria-label="Grey geometric star lattice border"></div>
    <div class="paper-rule paper-rule--lower"></div>
  </section>

</body>
</html>
```